VELTRIX GROUP
Project: VXG LOGO
VXG LOGO - Trade
VXG LOGO
Use same font as used in my logo
FAISAL NOORi
GENERAL MANAGER
RIYADH
info@veltrixgroup-example.com
VXGROUP VXGROUP
following changes on your design no #158 the logo upper and left side of the letter head company name bottom and left side of the letter haead The business cards are also in the above pattern. waiting for your immediate response. thanks.

```html
<!DOCTYPE html>
<html lang="en">
<head>
<meta charset="utf-8">
<title>Veltrix Group – Business Card</title>
<link rel="stylesheet" href="https://fonts.googleapis.com/css2?family=Exo+2:wght@500;600;700;800&display=swap">
<style>
  :root {
    --brand-blue: #2b57a7;
    --card-white: #ffffff;
    --backdrop: #5f5f5f;
    --card-edge: #d9d9d9;
  }
  * { margin: 0; padding: 0; box-sizing: border-box; }
  html, body {
    width: 1200px;
    height: 837px;
    overflow: hidden;
    background: var(--backdrop);
    font-family: "Exo 2", "Arial", sans-serif;
  }
  .business-card {
    position: absolute;
    left: 100px;
    top: 138px;
    width: 1000px;
    height: 560px;
    background: var(--card-white);
    border: 2px solid var(--card-edge);
    border-radius: 22px;
    overflow: hidden;
    color: var(--brand-blue);
  }
  .brand-wordmark {
    position: absolute;
    left: 46px;
    top: 30px;
    font-size: 150px;
    font-weight: 800;
    line-height: 1;
    letter-spacing: -2px;
  }
  .name-band {
    position: absolute;
    left: 0;
    top: 239px;
    width: 100%;
    height: 91px;
    background: var(--brand-blue);
    display: flex;
    align-items: center;
    justify-content: center;
  }
  .company-name {
    color: var(--card-white);
    font-size: 50px;
    font-weight: 600;
    letter-spacing: 6px;
  }
  .person {
    position: absolute;
    left: 46px;
    top: 396px;
    display: flex;
    flex-direction: column;
    align-items: flex-end;
  }
  .person-name {
    font-size: 42px;
    font-weight: 600;
    line-height: 1;
  }
  .person-title {
    margin-top: 8px;
    font-size: 22px;
    font-weight: 600;
    letter-spacing: 1px;
  }
  .contact {
    position: absolute;
    left: 558px;
    top: 382px;
    list-style: none;
    font-size: 24px;
    font-weight: 500;
    line-height: 33px;
  }
</style>
</head>
<body>
  <article class="business-card">
    <div class="brand-wordmark">VXG</div>
    <div class="name-band">
      <span class="company-name">VELTRIX GROUP</span>
    </div>
    <div class="person">
      <span class="person-name">FAISAL NOORi</span>
      <span class="person-title">GENERAL MANAGER</span>
    </div>
    <ul class="contact">
      <li class="contact-city">RIYADH</li>
      <li class="contact-phone">Phone: 966-555-0100</li>
      <li class="contact-fax">Fax: 966-555-0101</li>
      <li class="contact-email">Email: info@veltrixgroup-example.com</li>
    </ul>
  </article>
</body>
</html>
```